Property refurbishment & maintenance Business Card Design

Velkoran Ltd is a leading provider of domestic maintenance, building and refurbishment services. Founded in October 2009 by Milo Velkoran, we aim to provide our customers with exceptional home improvement and maintenance services whilst minimising the disruption and stress caused.
The building services we provide are of the very highest quality. We provide all of your customers with the peace of mind in knowing that they are dealing with experts in construction, renovation and decoration. This is because we are members of the Guild of Certified Tradecrafters (GCT). We have also had our credentials verified by Pledgeline and the UK government's Fair Seal scheme.
Target Market(s)
Private home owners,letting agents,tenants
Industry/Entity Type
Home Improvement
Contact Information for Business Card
Velkoran ltd.
Milo Velkoran
18 Brindle Cope Lane ,Waltham Cross,Herts,EN4 2QW,T.01632960517 M:07700900382
E. info@velkoran.co.uk. www.velkoran.co.uk

```html
<!DOCTYPE html>
<html lang="en">
<head>
<meta charset="utf-8">
<title>Velkoran Ltd — Business Card</title>
<link rel="stylesheet" href="https://fonts.googleapis.com/css2?family=Lato:wght@400;700;900&display=swap">
<style>
  :root {
    --backdrop: #3b3430;
    --card: #1c1c1d;
    --card-edge: #2a2a2b;
    --silver: #8d8f92;
    --teal: #3f9c8c;
    --amber: #e09a2c;
    --text-light: #d9d9d9;
    --text-muted: #a9a9a9;
    --divider: #3a3a3c;
  }
  html, body {
    margin: 0;
    width: 1200px;
    height: 827px;
    overflow: hidden;
    background: var(--backdrop);
    font-family: "Lato", sans-serif;
  }
  .canvas {
    position: relative;
    width: 1200px;
    height: 827px;
  }
  .card {
    position: absolute;
    top: 243px;
    width: 540px;
    height: 340px;
    background: var(--card);
    border: 1px solid var(--card-edge);
    border-radius: 4px;
    box-sizing: border-box;
  }
  .card--front { left: 40px; }
  .card--back { left: 620px; }

  .front-wordmark {
    position: absolute;
    left: 0; right: 0;
    top: 132px;
    text-align: center;
    font-weight: 700;
    font-size: 62px;
    letter-spacing: 4px;
    color: var(--silver);
  }
  .front-wordmark .mark-square {
    display: inline-block;
    width: 14px; height: 14px;
    background: var(--silver);
    margin-right: 16px;
    vertical-align: middle;
  }

  .back-wordmark {
    position: absolute;
    left: 28px;
    top: 148px;
    font-weight: 700;
    font-size: 30px;
    letter-spacing: 2px;
    color: var(--teal);
  }
  .back-wordmark .mark-square {
    display: inline-block;
    width: 8px; height: 8px;
    background: var(--teal);
    margin-right: 8px;
    vertical-align: middle;
  }
  .divider {
    position: absolute;
    left: 232px;
    top: 60px;
    width: 1px;
    height: 220px;
    background: var(--divider);
  }
  .contact {
    position: absolute;
    left: 252px;
    top: 72px;
    right: 16px;
    color: var(--text-light);
  }
  .contact__name {
    margin: 0;
    font-weight: 900;
    font-size: 21px;
    color: var(--amber);
  }
  .contact__role {
    margin: 2px 0 14px;
    font-size: 15px;
    color: var(--text-muted);
  }
  .contact__address {
    margin: 0 0 10px;
    font-size: 13px;
    line-height: 1.35;
  }
  .contact__list {
    list-style: none;
    margin: 0;
    padding: 0;
    font-size: 14px;
    line-height: 1.3;
  }
  .contact__list li {
    display: flex;
    align-items: center;
  }
  .contact__list .icon {
    width: 14px;
    height: 14px;
    margin-right: 8px;
    flex: none;
  }
  .contact__list .no-icon { padding-left: 22px; }
</style>
</head>
<body>
<main class="canvas">
  <section class="card card--front" aria-label="Card front">
    <div class="front-wordmark"><span class="mark-square"></span>VELKORAN</div>
  </section>

  <section class="card card--back" aria-label="Card back">
    <div class="back-wordmark"><span class="mark-square"></span>VELKORAN</div>
    <div class="divider"></div>
    <div class="contact">
      <h1 class="contact__name">Milo Velkoran</h1>
      <p class="contact__role">Manager</p>
      <p class="contact__address">Velkoran ltd. Milo Velkoran 18 Brindle Cope<br>Lane , Waltham Cross,Herts,EN4 2QW</p>
      <ul class="contact__list">
        <li>
          <svg class="icon" viewBox="0 0 14 14" aria-hidden="true">
            <rect x="1" y="5" width="12" height="8" rx="1.5" fill="none" stroke="var(--amber)" stroke-width="1.4"/>
            <path d="M3 5 Q7 1 11 5" fill="none" stroke="var(--amber)" stroke-width="1.4"/>
            <circle cx="7" cy="9" r="1.6" fill="var(--amber)"/>
          </svg>01632960517
        </li>
        <li>
          <svg class="icon" viewBox="0 0 14 14" aria-hidden="true">
            <rect x="3.5" y="1" width="7" height="12" rx="1.2" fill="none" stroke="var(--amber)" stroke-width="1.4"/>
            <circle cx="7" cy="10.8" r="0.9" fill="var(--amber)"/>
          </svg>07700900382
        </li>
        <li class="no-icon">info@velkoran.co.uk.</li>
        <li class="no-icon">www.velkoran.co.uk</li>
      </ul>
    </div>
  </section>
</main>
</body>
</html>
```